Tallow Creek Partners needs an email sign off and professional power point template

Newly formed company and we require:1. graphic email signature on our email , and2.a professional powerpoint template (title page and sub pages) and revamp of the attached powerpoint presentation I have uploaded our business car design (logo and contact details ) and a current powerpoint template we are currently working with. Also a brief of how we operateOur mantra is Discover, Develop, Deliver.

Target Market(s)

multinationals and mid size SME's requiring help to grown new markets or geographies for their business.

Colors
000000

Requirements
Must have
• the mantra..our phases of engagement around assisting clients is:
• 1. Discover
• 2. Develop
• 3. Deliver
Nice to have
• we differentiate ourselves form consultant by actually executing the plan for them (i.e. is the delivery phase)

```html
<!DOCTYPE html>
<html lang="en">
<head>
<meta charset="utf-8">
<title>Tallow Creek Partners – Email Signature</title>
<link rel="stylesheet" href="https://fonts.googleapis.com/css2?family=Montserrat:wght@400;500;600&display=swap">
<style>
  :root {
    --page-bg: #f3f4f6;
    --card-bg: #ffffff;
    --brand-blue: #2f6a8a;
    --art-light: #1f7fa6;
    --art-mid: #366882;
    --art-dark: #2d5673;
    --text-grey: #555a60;
    --icon-blue: #3b6683;
  }
  * { margin: 0; padding: 0; box-sizing: border-box; }
  html, body {
    width: 1200px;
    height: 1199px;
    overflow: hidden;
    background: var(--page-bg);
    font-family: "Montserrat", sans-serif;
  }
  .signature {
    position: absolute;
    left: 192px;
    top: 449px;
    width: 818px;
    height: 215px;
    background: var(--card-bg);
    box-shadow: 0 1px 4px rgba(0,0,0,0.08);
    overflow: hidden;
  }
  .signature__art {
    position: absolute;
    left: 0;
    top: 0;
    width: 320px;
    height: 215px;
    background: linear-gradient(90deg, var(--art-light) 0%, var(--art-mid) 45%, var(--art-dark) 100%);
  }
  .signature__brand {
    position: absolute;
    left: 0;
    top: 92px;
    width: 320px;
    text-align: center;
    color: #ffffff;
    font-weight: 500;
    font-size: 13px;
    line-height: 16px;
    letter-spacing: 0.05em;
    text-transform: uppercase;
  }
  .signature__company {
    position: absolute;
    left: 351px;
    top: 58px;
    color: var(--brand-blue);
    font-weight: 500;
    font-size: 19px;
    line-height: 21px;
    letter-spacing: 0.03em;
    text-transform: uppercase;
  }
  .signature__person {
    position: absolute;
    left: 351px;
    top: 139px;
  }
  .signature__name {
    color: var(--brand-blue);
    font-weight: 500;
    font-size: 19px;
    letter-spacing: 0.04em;
    text-transform: uppercase;
    line-height: 22px;
  }
  .signature__role {
    color: var(--text-grey);
    font-weight: 500;
    font-size: 13.5px;
    letter-spacing: 0.03em;
    text-transform: uppercase;
    line-height: 18px;
  }
  .signature__contacts {
    position: absolute;
    left: 616px;
    top: 138px;
    list-style: none;
  }
  .signature__contact {
    display: flex;
    align-items: center;
    height: 20.5px;
    color: var(--text-grey);
    font-size: 13px;
    white-space: nowrap;
  }
  .signature__icon {
    width: 12px;
    height: 12px;
    margin-right: 12px;
    flex: none;
  }
</style>
</head>
<body>
  <section class="signature">
    <div class="signature__art" role="img" aria-label="Illustration of a layered blue mountain range"></div>
    <div class="signature__brand">Tallow Creek<br>Partners</div>

    <div class="signature__company">Tallow Creek<br>Partners</div>

    <div class="signature__person">
      <div class="signature__name">Maren&nbsp; Holloway</div>
      <div class="signature__role">Principal</div>
    </div>

    <ul class="signature__contacts">
      <li class="signature__contact">
        <svg class="signature__icon" viewBox="0 0 12 12" aria-hidden="true">
          <path d="M8.5 0.8 L10 2.2 L8.6 3.8 L7.6 3.3 Q5.8 5.8 5.4 8.6 L6.5 8.9 L6.2 11 L4.2 11.2 Q3.2 6 7.6 0.8 Z" fill="var(--icon-blue)"/>
        </svg>
        555-014-2290
      </li>
      <li class="signature__contact">
        <svg class="signature__icon" viewBox="0 0 12 12" aria-hidden="true">
          <rect x="0.5" y="2.5" width="11" height="7.5" fill="var(--icon-blue)"/>
          <path d="M0.8 2.8 L6 6.8 L11.2 2.8" fill="none" stroke="#ffffff" stroke-width="0.9"/>
        </svg>
        maren@tallowcreek.ca
      </li>
      <li class="signature__contact">
        <svg class="signature__icon" viewBox="0 0 12 12" aria-hidden="true">
          <circle cx="6" cy="6" r="5.6" fill="var(--icon-blue)"/>
          <g fill="none" stroke="#ffffff" stroke-width="0.7">
            <ellipse cx="6" cy="6" rx="2.4" ry="5.4"/>
            <line x1="0.6" y1="6" x2="11.4" y2="6"/>
            <line x1="1.4" y1="3.4" x2="10.6" y2="3.4"/>
            <line x1="1.4" y1="8.6" x2="10.6" y2="8.6"/>
          </g>
        </svg>
        www.tallowcreek.ca
      </li>
    </ul>
  </section>
</body>
</html>
```